Harborline Cremations Business Cards

To create a business card for my company Harborline Cremations. Remember it is a cremation company.
We want to make sure people have a business card and information. Something modern, professional
100% Online
Prices starting at $695 all-inclusive (prices subject to change without notice).
A business card is the first point of contact with the prospective client.

Contact Information for Business Card

(305) 418-7260
www.HarborlineCremationsMiami.example
harborlinecremations@mailbox.example

Requirements
Must have
• 100% Online
Prices starting at $695 all-inclusive (prices subject to change without notice)

(305) 418-7260

Must match logo style
Should not have
• No black backgrounds. Please only use the white, orange and blue from the logo

```html
<!DOCTYPE html>
<html lang="en">
<head>
<meta charset="utf-8">
<title>Harborline Cremations – Business Card</title>
<link href="https://fonts.googleapis.com/css2?family=Lato:wght@400;700&display=swap" rel="stylesheet">
<style>
  :root {
    --orange-light: #e98d1f;
    --orange-dark: #e0601f;
    --orange-text: #e87d22;
    --blue: #229fd8;
    --white: #ffffff;
    --ink: #222222;
    --frame: #8a8a8a;
  }
  * { box-sizing: border-box; margin: 0; padding: 0; }
  html, body {
    width: 1045px; height: 1200px; overflow: hidden;
    background: var(--white);
    font-family: "Lato", Arial, sans-serif;
  }
  .card {
    position: absolute; left: 1px; width: 1026px; height: 577px;
    border: 1px solid var(--frame); overflow: hidden;
  }
  .card--front {
    top: 1px;
    background: linear-gradient(160deg, var(--orange-light) 0%, var(--orange-light) 35%, var(--orange-dark) 100%);
  }
  .card--back { top: 602px; background: var(--white); }

  .brand {
    position: absolute; text-align: center;
    font-weight: 700; text-transform: uppercase; line-height: 1.05;
  }
  .brand__dot { display: block; margin: 0 auto 26px; border-radius: 50%; }
  .brand--front { left: 0; right: 0; top: 120px; color: var(--white); font-size: 62px; letter-spacing: 6px; }
  .brand--front .brand__dot { width: 120px; height: 120px; background: var(--white); }
  .brand--back { left: 560px; width: 420px; top: 92px; color: var(--blue); font-size: 52px; letter-spacing: 5px; }
  .brand--back .brand__dot { width: 96px; height: 96px; background: var(--blue); }

  .tag {
    position: absolute; top: 469px; height: 66px;
    background: var(--blue); color: var(--white);
  }
  .tag--online {
    left: 0; width: 265px; border-top-right-radius: 22px;
    font-size: 31px; font-weight: 700; padding: 14px 0 0 48px;
  }
  .tag--price {
    right: 0; width: 444px; border-top-left-radius: 22px;
    padding: 10px 0 0 22px;
  }
  .tag__main { font-size: 22px; display: block; }
  .tag__note { font-size: 15px; display: block; margin-top: 3px; }

  .person {
    position: absolute; left: 77px; top: 290px;
    color: var(--orange-text); font-size: 38px; font-weight: 700;
  }
  .contacts { position: absolute; left: 77px; top: 370px; list-style: none; }
  .contacts__item {
    display: flex; align-items: center; height: 51px;
    font-size: 31px; color: var(--ink);
  }
  .contacts__icon { width: 32px; height: 32px; margin-right: 26px; flex: none; }
</style>
</head>
<body>
  <section class="card card--front">
    <div class="brand brand--front">
      <span class="brand__dot"></span>
      Harborline<br>Cremations
    </div>
    <div class="tag tag--online">100% Online</div>
    <div class="tag tag--price">
      <span class="tag__main">Prices starting at $695 all-inclusive</span>
      <span class="tag__note">(prices subject to change without notice)</span>
    </div>
  </section>

  <section class="card card--back">
    <div class="brand brand--back">
      <span class="brand__dot"></span>
      Harborline<br>Cremations
    </div>
    <h1 class="person">Person Name</h1>
    <ul class="contacts">
      <li class="contacts__item">
        <svg class="contacts__icon" viewBox="0 0 32 32" aria-hidden="true">
          <rect x="8" y="1" width="16" height="30" rx="4" fill="var(--orange-text)"/>
          <rect x="11" y="5" width="10" height="18" rx="1" fill="var(--white)"/>
          <circle cx="16" cy="27" r="1.8" fill="var(--white)"/>
        </svg>
        (305) 418-7260
      </li>
      <li class="contacts__item">
        <svg class="contacts__icon" viewBox="0 0 32 32" aria-hidden="true">
          <rect x="0" y="6" width="32" height="21" rx="2" fill="var(--orange-text)"/>
          <path d="M1 8 L16 19 L31 8" fill="none" stroke="var(--white)" stroke-width="2"/>
          <path d="M1 26 L12 16 M31 26 L20 16" stroke="var(--white)" stroke-width="1.5"/>
        </svg>
        www.HarborlineCremationsMiami.example
      </li>
      <li class="contacts__item">
        <svg class="contacts__icon" viewBox="0 0 32 32" aria-hidden="true">
          <circle cx="16" cy="16" r="13" fill="var(--orange-text)"/>
          <g fill="none" stroke="var(--white)" stroke-width="2">
            <ellipse cx="16" cy="16" rx="5" ry="12"/>
            <path d="M4 16 H28 M6 10 H26 M6 22 H26 M16 4 V28"/>
          </g>
        </svg>
        harborlinecremations@mailbox.example
      </li>
    </ul>
  </section>
</body>
</html>
```